Business Cards, Stationery and Envelope Design
The Law Office of Gavin T. Morrell, P.A.
Professional
Gavin T. Morrell, Esq., LL.M.
Attorney at Law
2847 Heronwood Commerce Boulevard
Suite 214
Sunrise, FL 33319
gavin@gtmlegalgroup-example.com
www.gtmlegalgroup-example.com
Want logo to be on the business card, stationery and envelope. Would like to see writing in black but also a little color in the card, stationery and envelope other than just in the logo.
Business Formation & Structuring
Purchase & Sale of Business
Contract Review & Preparation
Shareholder Agreements
Loan Transactions
Tax Matters
Real Estate Closings
.ai file now uploaded
Attached is a file with my logo. Please let me know if you need it in another format.

```html
<!DOCTYPE html>
<html lang="en">
<head>
<meta charset="utf-8">
<title>Gavin T. Morrell, P.A. — Business Cards</title>
<link href="https://fonts.googleapis.com/css2?family=Cinzel:wght@400;600&display=swap" rel="stylesheet">
<style>
:root{
  --bg:#e9e4dc;
  --green:#1f9a3c;
  --green-light:#3cc45a;
  --green-dark:#0f5a22;
  --black:#0b0b0b;
  --charcoal:#1c1c1c;
  --white:#ffffff;
  --ink:#111111;
  --grey:#bdbdbd;
}
*{box-sizing:border-box;margin:0;padding:0}
html,body{width:1200px;height:838px;overflow:hidden;background:var(--bg)}
body{position:relative;font-family:"Cinzel",serif}
.card{position:absolute;width:490px;height:290px;border-radius:16px;overflow:hidden;box-shadow:0 6px 14px rgba(0,0,0,.35)}
.card--front-dark{left:66px;top:148px;background:var(--black)}
.card--front-light{left:634px;top:148px;background:var(--white)}
.card--back-dark{left:66px;top:452px;background:linear-gradient(180deg,var(--charcoal),var(--black))}
.card--back-green{left:634px;top:452px;background:linear-gradient(160deg,var(--green-light),var(--green) 45%,var(--green-dark))}

.band{position:absolute;left:0;right:0;top:0;height:128px}
.card--front-dark .band{background:linear-gradient(180deg,var(--green-light),var(--green) 60%,var(--green-dark))}
.card--front-dark .band::after{content:"";position:absolute;left:0;right:0;bottom:0;height:3px;background:var(--white)}
.card--front-light .band{background:var(--white)}
.card--front-light .lower{position:absolute;left:0;right:0;top:128px;bottom:0;background:linear-gradient(180deg,var(--green-light),var(--green) 50%,var(--green-dark))}

.mark{position:absolute;display:flex;align-items:center;justify-content:center;font-family:"Cinzel",serif;font-weight:600;color:var(--white);background:var(--black);border:3px solid var(--white)}
.mark--small{left:24px;top:24px;width:88px;height:88px;font-size:26px}
.card--front-light .mark--small{border-color:var(--black)}
.mark--large{left:36px;top:52px;width:150px;height:150px;font-size:44px}
.card--back-green .mark--large{background:var(--white);color:var(--black);border-color:var(--white)}

.firm{position:absolute;left:128px;top:30px;right:20px;text-align:center}
.firm__pre{font-size:11px;letter-spacing:1px}
.firm__name{font-size:27px;letter-spacing:.5px;white-space:nowrap}
.card--front-dark .firm{color:var(--white)}
.card--front-light .firm{color:var(--ink)}

.attorney{position:absolute;left:128px;top:100px;right:20px;font-size:12px;white-space:nowrap}
.card--front-dark .attorney{color:var(--white);top:134px}
.card--front-light .attorney{color:var(--ink)}
.attorney .sep{margin:0 8px}
.rule{position:absolute;left:128px;right:20px;top:95px;height:1px}
.card--front-light .rule{background:var(--ink)}

.address{position:absolute;right:30px;top:172px;text-align:right;font-size:11.5px;line-height:15px;color:var(--white)}
.contact{position:absolute;right:30px;top:222px;text-align:right;font-size:10.5px;line-height:16px;color:var(--white);white-space:nowrap}
.contact .ico{display:inline-block;width:10px;height:10px;vertical-align:-1px;margin-right:4px}
.card--front-dark .ico{fill:var(--green-light)}
.card--front-light .ico{fill:var(--white)}
.contact .sep{margin:0 6px}

.services{position:absolute;left:210px;top:50px;list-style:none;font-size:12.5px;line-height:19px;color:var(--white)}
.services li{display:flex;align-items:center;gap:8px}
.services svg{width:12px;height:12px;flex:none}
.card--back-dark .services svg path{stroke:var(--green-light)}
.card--back-green .services svg path{stroke:var(--white)}

.sign{position:absolute;right:26px;bottom:20px;text-align:center;color:var(--white)}
.sign__pre{font-size:7px;letter-spacing:.6px}
.sign__name{font-size:13px}
.sign::before{content:"";display:block;height:1px;background:var(--grey);margin-bottom:3px}
</style>
</head>
<body>

<section class="card card--front-dark">
  <div class="band"></div>
  <div class="mark mark--small">GTM</div>
  <div class="firm">
    <div class="firm__pre">The Law Office of</div>
    <div class="firm__name">Gavin T. Morrell, P.A.</div>
  </div>
  <div class="attorney">Gavin T. Morrell, Esq., LL.M.<span class="sep">|</span>Attorney at Law</div>
  <div class="address">2847 Heronwood Commerce Boulevard<br>Suite 214, Sunrise, FL 33319</div>
  <div class="contact">
    <svg class="ico" viewBox="0 0 10 10"><rect width="10" height="10" rx="2"/></svg>954-555-0148<span class="sep">|</span><svg class="ico" viewBox="0 0 10 10"><rect width="10" height="10" rx="2"/></svg>954-555-0172<br>
    <svg class="ico" viewBox="0 0 10 10"><rect width="10" height="10" rx="2"/></svg>gavin@gtmlegalgroup-example.com<span class="sep">|</span><svg class="ico" viewBox="0 0 10 10"><rect width="10" height="10" rx="2"/></svg>www.gtmlegalgroup-example.com
  </div>
</section>

<section class="card card--front-light">
  <div class="band"></div>
  <div class="lower"></div>
  <div class="mark mark--small">GTM</div>
  <div class="firm">
    <div class="firm__pre">The Law Office of</div>
    <div class="firm__name">Gavin T. Morrell, P.A.</div>
  </div>
  <div class="rule"></div>
  <div class="attorney">Gavin T. Morrell, Esq., LL.M.<span class="sep">|</span>Attorney at Law</div>
  <div class="address">2847 Heronwood Commerce Boulevard<br>Suite 214, Sunrise, FL 33319</div>
  <div class="contact">
    <svg class="ico" viewBox="0 0 10 10"><rect width="10" height="10" rx="2"/></svg>954-555-0148<span class="sep">|</span><svg class="ico" viewBox="0 0 10 10"><rect width="10" height="10" rx="2"/></svg>954-555-0172<br>
    <svg class="ico" viewBox="0 0 10 10"><rect width="10" height="10" rx="2"/></svg>gavin@gtmlegalgroup-example.com<span class="sep">|</span><svg class="ico" viewBox="0 0 10 10"><rect width="10" height="10" rx="2"/></svg>www.gtmlegalgroup-example.com
  </div>
</section>

<section class="card card--back-dark">
  <div class="mark mark--large">GTM</div>
  <ul class="services">
    <li><svg viewBox="0 0 12 12"><path d="M1 6l3.5 4L11 1" fill="none" stroke-width="2"/></svg>Business Formation &amp; Structuring</li>
    <li><svg viewBox="0 0 12 12"><path d="M1 6l3.5 4L11 1" fill="none" stroke-width="2"/></svg>Purchase &amp; Sale of Business</li>
    <li><svg viewBox="0 0 12 12"><path d="M1 6l3.5 4L11 1" fill="none" stroke-width="2"/></svg>Contract Review &amp; Preparation</li>
    <li><svg viewBox="0 0 12 12"><path d="M1 6l3.5 4L11 1" fill="none" stroke-width="2"/></svg>Shareholder Agreements</li>
    <li><svg viewBox="0 0 12 12"><path d="M1 6l3.5 4L11 1" fill="none" stroke-width="2"/></svg>Loan Transactions</li>
    <li><svg viewBox="0 0 12 12"><path d="M1 6l3.5 4L11 1" fill="none" stroke-width="2"/></svg>Tax Matters</li>
    <li><svg viewBox="0 0 12 12"><path d="M1 6l3.5 4L11 1" fill="none" stroke-width="2"/></svg>Real Estate Closings</li>
  </ul>
  <div class="sign"><div class="sign__pre">The Law Office of</div><div class="sign__name">Gavin T. Morrell, P.A.</div></div>
</section>

<section class="card card--back-green">
  <div class="mark mark--large">GTM</div>
  <ul class="services">
    <li><svg viewBox="0 0 12 12"><path d="M1 6l3.5 4L11 1" fill="none" stroke-width="2"/></svg>Business Formation &amp; Structuring</li>
    <li><svg viewBox="0 0 12 12"><path d="M1 6l3.5 4L11 1" fill="none" stroke-width="2"/></svg>Purchase &amp; Sale of Business</li>
    <li><svg viewBox="0 0 12 12"><path d="M1 6l3.5 4L11 1" fill="none" stroke-width="2"/></svg>Contract Review &amp; Preparation</li>
    <li><svg viewBox="0 0 12 12"><path d="M1 6l3.5 4L11 1" fill="none" stroke-width="2"/></svg>Shareholder Agreements</li>
    <li><svg viewBox="0 0 12 12"><path d="M1 6l3.5 4L11 1" fill="none" stroke-width="2"/></svg>Loan Transactions</li>
    <li><svg viewBox="0 0 12 12"><path d="M1 6l3.5 4L11 1" fill="none" stroke-width="2"/></svg>Tax Matters</li>
    <li><svg viewBox="0 0 12 12"><path d="M1 6l3.5 4L11 1" fill="none" stroke-width="2"/></svg>Real Estate Closings</li>
  </ul>
  <div class="sign"><div class="sign__pre">The Law Office of</div><div class="sign__name">Gavin T. Morrell, P.A.</div></div>
</section>

</body>
</html>
```